Vorel constructions

We are predominantly a residential home builder based in Melbourne, Victoria Australia. We construct houses, apartments, townhouses, multi-unit developments.

The name of the company is "Vorel Constructions"
My company believes in building unique construction projects mainly residential homes. The target customers are upmarket Melbourne residents/investors.

I want the brand name "Vorel" to be part of the logo. There's no need to put the word construction in the logo at this stage.

I would also like some ideas for a slogan e.g. "Just build it." or "We build quality homes." But I would like something unique and different for a slogan not the same old cliche.

vorelconstructions.example.com.au
e: tmelo@vorelconstructions.example.com.au
M: 0417305862
Address: 8/3 Fenwick Lane Clayton VIC 3168

Director:Mr Dinesh Malarkodiyan

```html
<!DOCTYPE html>
<html lang="en">
<head>
<meta charset="utf-8">
<title>Vorel Constructions</title>
<link rel="stylesheet" href="https://fonts.googleapis.com/css2?family=Oswald:wght@300;400&display=swap">
<style>
  :root {
    --teal: #4a9893;
    --teal-light: #50c6c0;
    --cyan: #57fef6;
    --band: #3d4a4b;
    --white: #ffffff;
    --shadow: rgba(0, 0, 0, 0.45);
  }
  * { margin: 0; padding: 0; box-sizing: border-box; }
  html, body {
    width: 1200px;
    height: 741px;
    overflow: hidden;
    background: var(--teal);
  }
  .card {
    position: relative;
    width: 1200px;
    height: 741px;
    overflow: hidden;
    background: var(--teal);
  }
  .pattern-field {
    position: absolute;
    left: 0;
    width: 1200px;
    height: 200px;
    background: linear-gradient(135deg, var(--teal) 0%, var(--teal-light) 50%, var(--teal) 100%);
  }
  .pattern-field--top { top: 0; }
  .pattern-field--bottom { bottom: 0; }
  .brand-band {
    position: absolute;
    left: 0;
    top: 192px;
    width: 1200px;
    height: 363px;
    background: var(--band);
    box-shadow: 0 0 34px 10px var(--shadow);
  }
  .brand-name {
    position: absolute;
    left: 0;
    top: 36px;
    width: 1200px;
    text-align: center;
    font-family: "Oswald", sans-serif;
    font-weight: 400;
    font-size: 176px;
    line-height: 1.2;
    color: var(--cyan);
    letter-spacing: 4px;
  }
  .slogan {
    position: absolute;
    left: 0;
    top: 262px;
    width: 1200px;
    text-align: center;
    font-family: "Oswald", sans-serif;
    font-weight: 300;
    font-size: 31px;
    line-height: 1.2;
    color: var(--white);
    letter-spacing: 0.6px;
    white-space: nowrap;
  }
</style>
</head>
<body>
  <main class="card">
    <div class="pattern-field pattern-field--top" role="img" aria-label="Chevron stripe pattern in teal and bright cyan"></div>
    <div class="pattern-field pattern-field--bottom" role="img" aria-label="Chevron stripe pattern in teal and bright cyan"></div>
    <section class="brand-band">
      <h1 class="brand-name">Vorel</h1>
      <p class="slogan">“WE DONT JUST BUILD HOMES, WE BUILD LASTING MASTERPIECES”</p>
    </section>
  </main>
</body>
</html>
```